Update Business Card Design Project

We've been in business nearly 15 years and about 10 years ago developed a brand that is now well recognized. The business card is boring, too much print and nothing that says 'We are TRULY SPLENDID' right off the mark.
We are a fun store, lots of new things on a regular basis. Especially in kitchen goods where the colours are strong and the emphasis is on pretty and practical. We like to have both!
Hi there,
Target Market(s)
Store customers and suppliers
Demographics aged 40-70yrs, mid to high income, mostly women or couples, rural setting but in the 'shopping district' of our region. 1 hour to nearest city.
Industry/Entity Type
Business
Requirements
Nice to have
- Incorporate the logo, if possible

```html
<!DOCTYPE html>
<html lang="en">
<head>
<meta charset="utf-8">
<title>Truly Splendid — Business Card</title>
<link rel="stylesheet" href="https://fonts.googleapis.com/css2?family=Arimo:wght@400;700&display=swap">
<style>
  :root {
    --backdrop: #3a3a3a;
    --gold: #b8731c;
    --gold-light: #e2a24a;
    --gold-dark: #a8620f;
    --card-white: #ffffff;
    --text-gold: #b06c1a;
  }
  * { box-sizing: border-box; margin: 0; padding: 0; }
  html, body {
    width: 1200px; height: 871px; overflow: hidden;
    background: var(--backdrop);
    font-family: "Arimo", Arial, sans-serif;
  }
  .stage {
    width: 1200px; height: 871px;
    display: flex; align-items: center; justify-content: center; gap: 40px;
  }
  .card {
    width: 520px; height: 297px;
    border-radius: 18px;
    position: relative;
    overflow: hidden;
  }
  /* Back of card */
  .card--back {
    background: linear-gradient(135deg, var(--gold-light) 0%, var(--gold) 45%, var(--gold-dark) 100%);
    color: var(--card-white);
    display: flex; flex-direction: column; align-items: center; justify-content: center;
  }
  .back-brand {
    display: flex; align-items: center; gap: 12px;
    font-weight: 700; font-size: 34px; letter-spacing: 2px; text-transform: uppercase;
  }
  .brand-square { width: 22px; height: 22px; background: currentColor; }
  .back-web {
    position: absolute; bottom: 38px; left: 0; right: 0;
    text-align: center; font-size: 17px; letter-spacing: 6px;
  }
  /* Front of card */
  .card--front {
    background: var(--card-white);
    color: var(--text-gold);
    display: flex; align-items: center;
    padding: 0 34px;
  }
  .front-brand {
    width: 230px;
    display: flex; flex-direction: column; align-items: center; gap: 10px;
  }
  .front-brand__name {
    display: flex; align-items: center; gap: 10px;
    font-weight: 700; font-size: 27px; letter-spacing: 1px; text-transform: uppercase;
  }
  .front-brand__name .brand-square { width: 16px; height: 16px; }
  .front-brand__tagline {
    font-size: 12px; letter-spacing: 3px; text-transform: uppercase;
  }
  .divider {
    width: 1.5px; height: 170px; background: var(--text-gold);
    margin: 0 16px 0 24px;
  }
  .contact { font-size: 13px; line-height: 1.3; }
  .contact__address { margin-bottom: 12px; }
  .contact__phones { font-weight: 700; font-size: 15px; margin-bottom: 12px; line-height: 1.35; }
</style>
</head>
<body>
  <main class="stage">
    <section class="card card--back" aria-label="Card back">
      <div class="back-brand"><span class="brand-square"></span>Truly Splendid</div>
      <p class="back-web">www.trulysplendid.ca</p>
    </section>

    <section class="card card--front" aria-label="Card front">
      <div class="front-brand">
        <div class="front-brand__name"><span class="brand-square"></span>Truly Splendid</div>
        <p class="front-brand__tagline">Bed Bath &amp; Home</p>
      </div>
      <div class="divider"></div>
      <div class="contact">
        <p class="contact__address">Harbour Lane Plaza,<br>4120 Orchard Street<br>Maple Cove,<br>Nova Scotia, B0P 1X0</p>
        <p class="contact__phones">1 800 555 0142<br>1 902 555 0178</p>
        <p class="contact__web">hello@trulysplendid.ca<br>www.trulysplendid.ca</p>
      </div>
    </section>
  </main>
</body>
</html>
```